Gift Cards in the Mail Envelope

Mailing out gift cards in the envelope. Need an eye popping envelope. Please look at the enclosed images. The envelope should look like that.

Low design quality

```html
<!DOCTYPE html>
<html lang="en">
<head>
<meta charset="utf-8">
<title>Gift Card Mailer Envelope</title>
<link rel="stylesheet" href="https://fonts.googleapis.com/css2?family=Montserrat:wght@700;800&display=swap">
<style>
  :root {
    --backdrop: #777973;
    --envelope-pink: #e845a4;
    --envelope-pink-shade: #d93d97;
    --ink-dark: #262626;
    --ink-light: #f2f2f2;
  }
  * { margin: 0; padding: 0; box-sizing: border-box; }
  html, body {
    width: 1200px;
    height: 982px;
    overflow: hidden;
    background: var(--backdrop);
    font-family: "Montserrat", Arial, sans-serif;
  }
  .canvas {
    position: relative;
    width: 1200px;
    height: 982px;
  }
  .envelope-front {
    position: absolute;
    left: 252px;
    top: 363px;
    width: 332px;
    height: 228px;
    overflow: hidden;
  }
  .front-band-top {
    height: 114px;
    background: var(--envelope-pink);
    position: relative;
  }
  .front-band-bottom {
    height: 114px;
    background: var(--ink-dark);
    position: relative;
  }
  .front-word {
    position: absolute;
    left: 0;
    width: 100%;
    text-align: center;
    font-weight: 800;
    font-size: 42px;
    line-height: 1;
    letter-spacing: 0.5px;
  }
  .front-word--gift { color: var(--ink-dark); bottom: 9px; }
  .front-word--card { color: var(--ink-light); top: 10px; }
  .envelope-back {
    position: absolute;
    left: 626px;
    top: 363px;
    width: 333px;
    height: 229px;
  }
  .envelope-back svg { display: block; }
  .flap-label {
    position: absolute;
    left: 0;
    width: 100%;
    text-align: center;
    font-weight: 700;
    line-height: 1;
  }
  .flap-label--small { top: 55px; font-size: 8.5px; color: var(--ink-dark); }
  .flap-label--large { top: 66px; font-size: 16.5px; color: var(--ink-light); }
</style>
</head>
<body>
<main class="canvas">
  <section class="envelope-front" aria-label="Envelope front">
    <div class="front-band-top"><p class="front-word front-word--gift">Gift</p></div>
    <div class="front-band-bottom"><p class="front-word front-word--card">Card</p></div>
  </section>

  <section class="envelope-back" aria-label="Envelope back">
    <svg width="333" height="229" viewBox="0 0 333 229" aria-hidden="true">
      <rect x="0" y="0" width="333" height="229" fill="var(--envelope-pink)"/>
      <path d="M1 1 L28 78 Q33 89 46 89 L287 89 Q298 89 302 78 L332 1"
            fill="none" stroke="var(--envelope-pink-shade)" stroke-width="1.2"/>
      <path d="M34 90 L2 226 M296 90 L331 226"
            fill="none" stroke="var(--envelope-pink-shade)" stroke-width="1"/>
    </svg>
    <p class="flap-label flap-label--small">Gift Awaits</p>
    <p class="flap-label flap-label--large">Open Me</p>
  </section>
</main>
</body>
</html>
```